A clean crisp business card for a Landscape Construction company. Designed to be easy to read contact/ info and also be appealing/interesting, unlike a traditional business card.

Industry/Entity Type

Landscape Construction

Contact Information for Business Card

Company name : Bramblecrest Landscape Construction, phone number: (877) 62Vales, website:Bramblecrestlandscapes.example, Email, sales@bramblecrestlandscapes.example

Requirements
Nice to have
• Luxurious finishes/ details…. Icons or emblems next to contact info
Should not have
• Clipart or general pictures

```html
<!DOCTYPE html>
<html lang="en">
<head>
<meta charset="utf-8">
<title>Bramblecrest Landscape Construction — Business Card</title>
<link rel="stylesheet" href="https://fonts.googleapis.com/css2?family=Cinzel:wght@500;600&family=Lato:wght@400;700&display=swap">
<style>
  :root {
    --canvas: #2b2b2d;
    --brand-blue: #1a68c2;
    --leaf-green: #8cc63f;
    --paper: #ffffff;
  }
  * { box-sizing: border-box; margin: 0; padding: 0; }
  html, body { width: 1200px; height: 1015px; overflow: hidden; }
  body {
    background: var(--canvas);
    position: relative;
    font-family: "Lato", sans-serif;
  }
  .card {
    position: absolute;
    left: 240px;
    width: 720px;
    height: 410px;
    overflow: hidden;
    background: var(--brand-blue);
    box-shadow: 0 10px 30px rgba(0,0,0,0.45);
  }
  .card--front { top: 60px; }
  .card--back { top: 545px; }

  /* Brand lockup */
  .brand-dot {
    width: 46px; height: 46px;
    border-radius: 50%;
    background: var(--leaf-green);
  }
  .brand-name {
    font-family: "Cinzel", serif;
    font-weight: 600;
    text-transform: uppercase;
    text-align: center;
    line-height: 1.15;
    letter-spacing: 2px;
    white-space: nowrap;
  }
  .brand-name small { display: block; font-size: 0.42em; letter-spacing: 6px; }

  /* Front */
  .front-identity {
    position: absolute;
    inset: 0;
    display: flex;
    flex-direction: column;
    align-items: center;
    justify-content: center;
    gap: 18px;
  }
  .card--front .brand-name { color: var(--paper); font-size: 44px; }

  /* Back */
  .back-art { position: absolute; inset: 0; }
  .holder {
    position: absolute;
    left: 60px; top: 95px;
    color: var(--paper);
  }
  .holder-name {
    font-family: "Cinzel", serif;
    font-weight: 600;
    font-size: 26px;
    letter-spacing: 1.5px;
  }
  .holder-role { font-size: 18px; margin-top: 2px; }
  .address {
    position: absolute;
    left: 60px; top: 212px;
    color: var(--paper);
    font-style: normal;
    font-size: 17px;
    line-height: 1.3;
  }
  .contacts {
    position: absolute;
    left: 60px; top: 278px;
    list-style: none;
    color: var(--paper);
    font-size: 15px;
    line-height: 1.6;
  }
  .contacts li { display: flex; align-items: center; gap: 10px; }
  .contacts svg { width: 16px; height: 16px; flex: none; }
  .back-brand {
    position: absolute;
    left: 440px; top: 115px;
    width: 280px;
    display: flex;
    flex-direction: column;
    align-items: center;
    gap: 14px;
  }
  .card--back .brand-name { color: var(--brand-blue); font-size: 26px; }
  .card--back .brand-name small { color: var(--leaf-green); letter-spacing: 2.5px; font-size: 0.44em; }
</style>
</head>
<body>

<section class="card card--front" aria-label="Card front">
  <div class="front-identity">
    <span class="brand-dot"></span>
    <p class="brand-name">Bramblecrest<small>Landscape Construction</small></p>
  </div>
</section>

<section class="card card--back" aria-label="Card back">
  <svg class="back-art" viewBox="0 0 720 410" aria-hidden="true">
    <circle cx="600" cy="170" r="250" fill="var(--paper)"/>
    <path d="M385 20 A 262 262 0 0 0 495 405" fill="none" stroke="var(--leaf-green)" stroke-width="5" stroke-linecap="round"/>
  </svg>

  <div class="holder">
    <h1 class="holder-name">Dana Whitfield</h1>
    <p class="holder-role">Managing Director</p>
  </div>

  <address class="address">418 Fernhollow Road<br>Ashbury, 97455</address>

  <ul class="contacts">
    <li>
      <svg viewBox="0 0 24 24" fill="none" stroke="currentColor" stroke-width="2"><path d="M5 3h4l2 5-3 2a12 12 0 0 0 6 6l2-3 5 2v4a2 2 0 0 1-2 2A18 18 0 0 1 3 5a2 2 0 0 1 2-2z"/></svg>
      (877) 62Vales
    </li>
    <li>
      <svg viewBox="0 0 24 24" fill="none" stroke="currentColor" stroke-width="2"><rect x="2" y="5" width="20" height="14"/><path d="M2 5l10 8 10-8"/></svg>
      sales@bramblecrestlandscapes.example
    </li>
    <li>
      <svg viewBox="0 0 24 24" fill="none" stroke="currentColor" stroke-width="2"><circle cx="12" cy="12" r="10"/><path d="M2 12h20M12 2c3 3 3 17 0 20M12 2c-3 3-3 17 0 20"/></svg>
      Bramblecrestlandscapes.example
    </li>
  </ul>

  <div class="back-brand">
    <span class="brand-dot"></span>
    <p class="brand-name">Bramblecrest<small>Landscape Construction</small></p>
  </div>
</section>

</body>
</html>
```